Business Card Design

We have our logo and everything in place. Looking to have a layout for our new business cards designed. These will be printed with a matte finish, possibly rounded corners, and looking to incorporate some cool spot UV layers into the design.

Ive uploaded the existing card front and back as well as our logo.

Card Size Will Be 3.5" x 2"

```html
<!DOCTYPE html>
<html lang="en">
<head>
<meta charset="utf-8">
<title>Alderline Deck and Rail — Business Card</title>
<link rel="stylesheet" href="https://fonts.googleapis.com/css2?family=Cormorant+Garamond:wght@500&display=swap">
<style>
  :root {
    --card-black: #0b0c0d;
    --pattern-tone: #1b1d1f;
    --ink-white: #ffffff;
  }
  html, body {
    margin: 0;
    padding: 0;
    width: 1200px;
    height: 686px;
    overflow: hidden;
    background: var(--card-black);
  }
  .card {
    position: relative;
    width: 1200px;
    height: 686px;
    overflow: hidden;
    background: var(--card-black);
  }
  .card__pattern {
    position: absolute;
    inset: 0;
    background: radial-gradient(ellipse at 50% 50%, var(--pattern-tone) 0%, var(--card-black) 85%);
  }
  .card__brand {
    position: absolute;
    left: 0;
    right: 0;
    top: 190px;
    text-align: center;
    color: var(--ink-white);
    font-family: "Cormorant Garamond", serif;
    font-weight: 500;
  }
  .brand__name {
    display: block;
    font-size: 150px;
    line-height: 1;
  }
  .brand__tagline {
    display: block;
    margin-top: 40px;
    font-size: 40px;
    letter-spacing: 0.12em;
    text-transform: uppercase;
    line-height: 1;
  }
</style>
</head>
<body>
  <main class="card">
    <div class="card__pattern" role="img" aria-label="Dark tonal damask scroll pattern covering the card background"></div>
    <div class="card__brand">
      <span class="brand__name">Alderline</span>
      <span class="brand__tagline">Deck and Rail</span>
    </div>
  </main>
</body>
</html>
```